Thank you for shopping with us business card

We would like a thank you card for our rebranded business. We used to be "Brindle Goods" but are now "Marlow Finds. Old thank you card and new logo will be attached for reference. New thank you card does not have to be same design as old thank you card, but please use new logo.
Shopmart URL is now marlowfinds.shopmart.example
Instagram is @Marlow_Finds
Email is marlowfinds@mailbox.example
Thank you!

Contact Information for Business Card

Shopmart site, email, Instagram

```html
<!DOCTYPE html>
<html lang="en">
<head>
<meta charset="UTF-8">
<title>Marlow Finds – Thank You Card</title>
<link href="https://fonts.googleapis.com/css2?family=Josefin+Sans:wght@400;600&family=Montserrat:wght@800&display=swap" rel="stylesheet">
<style>
  :root {
    --page: #e6e3de;
    --card: #050505;
    --ink: #ffffff;
    --band-text: #0a0a0a;
    --shop: #f1641e;
    --social: #d6297a;
    --mail: #ffffff;
  }
  * { margin: 0; padding: 0; box-sizing: border-box; }
  html, body {
    width: 1200px; height: 900px; overflow: hidden;
    background: var(--page);
    font-family: "Josefin Sans", "Helvetica Neue", Arial, sans-serif;
  }
  .sheet {
    width: 1200px; height: 900px;
    display: flex; flex-direction: column;
    align-items: center; justify-content: center;
    gap: 44px;
  }
  .card {
    position: relative;
    width: 640px; height: 366px;
    background: var(--card);
    border-radius: 34px;
    overflow: hidden;
    color: var(--ink);
    box-shadow: 0 14px 30px rgba(0,0,0,.25);
  }
  .thanks-band {
    position: absolute; top: 58px; left: 0;
    height: 44px;
    padding: 0 52px 0 34px;
    background: var(--ink);
    clip-path: polygon(0 0, 100% 0, calc(100% - 26px) 100%, 0 100%);
    display: flex; align-items: center;
  }
  .thanks-band h1 {
    font-family: "Montserrat", "Arial Black", sans-serif;
    font-weight: 800; font-size: 17px;
    letter-spacing: .4px; color: var(--band-text);
    white-space: nowrap;
  }
  .message {
    position: absolute; top: 130px; left: 52px;
    font-size: 16px; line-height: 30px;
    letter-spacing: .2px;
  }
  .contacts {
    position: absolute; top: 252px; left: 52px;
    list-style: none;
    font-size: 15px; line-height: 30px;
  }
  .contacts li { display: flex; align-items: center; gap: 10px; }
  .dot { width: 17px; height: 17px; border-radius: 50%; flex: none; }
  .dot--shop { background: var(--shop); }
  .dot--social { background: var(--social); }
  .dot--mail { background: var(--mail); display: flex; align-items: center; justify-content: center; }
  .brand-name {
    font-family: "Josefin Sans", "Helvetica Neue", Arial, sans-serif;
    font-weight: 600; text-transform: uppercase;
    color: var(--ink); letter-spacing: .5px;
    white-space: nowrap;
  }
  .card--front .brand-name {
    position: absolute; top: 190px; left: 420px; right: 30px;
    text-align: center;
    font-size: 23px;
  }
  .card--back { display: flex; align-items: center; justify-content: center; }
  .card--back .brand-name { font-size: 32px; }
</style>
</head>
<body>
<main class="sheet">
  <section class="card card--front">
    <div class="thanks-band"><h1>THANK YOU FOR YOUR PURCHASE</h1></div>
    <p class="message">
      Your Purchase Made My Day And<br>
      I Hope This Package Brightens Your.<br>
      Please Come Back And Leave A Review!
    </p>
    <ul class="contacts">
      <li><span class="dot dot--shop"></span>marlowfinds.shopmart.example</li>
      <li><span class="dot dot--social"></span>@Marlow_Finds</li>
      <li><span class="dot dot--mail">
        <svg width="11" height="8" viewBox="0 0 11 8" aria-hidden="true">
          <rect x=".5" y=".5" width="10" height="7" fill="none" stroke="#050505" stroke-width="1"/>
          <polyline points=".5,.5 5.5,4.5 10.5,.5" fill="none" stroke="#050505" stroke-width="1"/>
        </svg>
      </span>marlowfinds@mailbox.example</li>
    </ul>
    <p class="brand-name">Marlow Finds</p>
  </section>

  <section class="card card--back">
    <p class="brand-name">Marlow Finds</p>
  </section>
</main>
</body>
</html>
```